Design Cloud for Core Values & Attributes

See Image Example Below "Word Cloud" this is what we would like this to look like.
The second image is all of the Core Value and Attributes I will list below.
CORE VALUES need to be the bigger words (based off the image I sent) Capitalized, BOLD, Navy
Independence, Capitalism, Trust, Fun, Safety, Growth
ATTRIBUTES need to be the smaller words, lower case, non-bold, lighter blue mixed in (based off the image I sent):
Humility, Consistency, Open Mindedness, Curiosity, Selflessness, Caring, Conscientiousness, Honorable, Cunning, Competitive, Compartmentalization, Innovative, Perseverance, Authenticity, Decisiveness, Self-efficacy, Accountability, Generosity, Humor, Optimism, Resilience, Inclusive, Insouciance to what others think, Courage, Decisive, Curious, Integrity

```html
<!DOCTYPE html>
<html lang="en">
<head>
<meta charset="utf-8">
<title>Core Values</title>
<link rel="stylesheet" href="https://fonts.googleapis.com/css2?family=Archivo+Black&family=Bebas+Neue&family=Montserrat:wght@500&display=swap">
<style>
  :root {
    --navy: #2b3479;
    --red: #9b1a35;
    --ink: #1f1f24;
    --paper: #fafafb;
    --paper-shade: #eeeff2;
    --page: #ffffff;
  }
  html, body {
    margin: 0;
    width: 1200px;
    height: 1200px;
    overflow: hidden;
    background: var(--page);
  }
  .poster {
    position: absolute;
    left: 122px;
    top: 231px;
    width: 967px;
    height: 747px;
    display: block;
  }
  .paper { fill: url(#paperTone); }
  .frame { fill: none; stroke: var(--red); stroke-width: 2.5; }
  .banner { fill: var(--navy); }
  .banner-title { font-family: "Archivo Black", "Arial Black", sans-serif; font-size: 60px; fill: #fff; }
  .value { font-family: "Bebas Neue", "Oswald", sans-serif; }
  .value--navy { fill: var(--navy); }
  .value--red { fill: var(--red); }
  .attr { font-family: "Montserrat", sans-serif; font-weight: 500; fill: var(--ink); }
  .attr--light { fill: #fff; }
  .accent-bar { fill: var(--red); }
  .box-navy { fill: none; stroke: var(--navy); stroke-width: 2.5; }
  .box-red { fill: none; stroke: var(--red); stroke-width: 2.5; }
  .tile-navy { fill: var(--navy); }
  .tile-red { fill: var(--red); }
  .icon-area { opacity: 0.18; }
</style>
</head>
<body>
<svg class="poster" viewBox="0 0 967 747" xmlns="http://www.w3.org/2000/svg">
  <defs>
    <linearGradient id="paperTone" x1="0" y1="0" x2="1" y2="1">
      <stop offset="0" stop-color="var(--paper)"/>
      <stop offset="0.5" stop-color="#ffffff"/>
      <stop offset="1" stop-color="var(--paper-shade)"/>
    </linearGradient>
  </defs>

  <rect class="paper" x="0" y="0" width="967" height="747"/>
  <rect class="frame" x="16" y="16" width="926" height="705"/>

  <!-- header tab -->
  <path class="banner" d="M206 0 H752 L731 92 Q727 108 709 108 H259 Q241 108 237 92 Z"/>
  <text class="banner-title" x="479" y="81" text-anchor="middle" textLength="444" lengthAdjust="spacingAndGlyphs">CORE VALUES</text>

  <!-- independence -->
  <text class="value value--navy" x="76" y="253" font-size="96" textLength="427" lengthAdjust="spacingAndGlyphs">INDEPENDENCE</text>
  <rect class="accent-bar" x="76" y="269" width="2.5" height="43"/>
  <text class="attr" x="91" y="285" font-size="20" textLength="412" lengthAdjust="spacingAndGlyphs">Humility Authenticity Curiosity Cunning</text>
  <text class="attr" x="91" y="311" font-size="20" textLength="398" lengthAdjust="spacingAndGlyphs">Selflessness Decisiveness Self-efficacy</text>
  <rect class="tile-red icon-area" x="519" y="186" width="125" height="122" rx="10" role="img" aria-label="Icon of a hand holding a flag"/>

  <!-- trust -->
  <rect class="tile-navy" x="76" y="332" width="48" height="54" role="img" aria-label="Handshake with shield icon"/>
  <rect class="box-navy" x="77" y="333" width="559" height="52"/>
  <text class="value value--red" x="131" y="376" font-size="48" textLength="88" lengthAdjust="spacingAndGlyphs">TRUST</text>
  <text class="attr" x="226" y="355" font-size="15.5" textLength="330" lengthAdjust="spacingAndGlyphs">Humility  Consistency  Open mindedness</text>
  <text class="attr" x="226" y="375" font-size="15.5" textLength="394" lengthAdjust="spacingAndGlyphs">Curiosity  Selflessness Caring  Conscientiousness</text>

  <!-- growth -->
  <text class="value value--red" transform="translate(732 431) rotate(-90)" x="0" y="0" font-size="100" textLength="245" lengthAdjust="spacingAndGlyphs">GROWTH</text>
  <path class="box-red" d="M734 187.5 H888 V428 H734"/>
  <g class="attr" font-size="18">
    <text x="743" y="214">Humility</text>
    <text x="743" y="243">Accountability</text>
    <text x="743" y="272">Curiosity</text>
    <text x="743" y="301">Generosity</text>
    <text x="743" y="330">Caring</text>
    <text x="743" y="359">Innovative</text>
    <text x="743" y="388">Perseverance</text>
    <text x="743" y="417">Honorable</text>
  </g>

  <!-- fun -->
  <text class="value value--red" x="72" y="546" font-size="204" textLength="230" lengthAdjust="spacingAndGlyphs">FUN</text>
  <rect class="tile-navy icon-area" x="319" y="402" width="136" height="145" rx="12" role="img" aria-label="Icon of two people with a smiling speech bubble"/>
  <g class="attr" font-size="17">
    <text x="467" y="417">Humor</text>
    <text x="467" y="438">Optimism</text>
    <text x="467" y="459">Humility</text>
    <text x="467" y="480">Resilience</text>
    <text x="467" y="502">Inclusive</text>
    <text x="467" y="523">Insouciance to what</text>
    <text x="467" y="544">others think Caring</text>
  </g>

  <!-- safety -->
  <rect class="tile-red icon-area" x="594" y="414" width="90" height="89" rx="10" role="img" aria-label="Icon of a worker in a hard hat with a shield"/>
  <text class="value value--navy" x="699" y="506" font-size="89" textLength="195" lengthAdjust="spacingAndGlyphs">SAFETY</text>
  <rect class="accent-bar" x="657" y="512" width="2" height="35"/>
  <text class="attr" x="668" y="529" font-size="13" textLength="222" lengthAdjust="spacingAndGlyphs">Courage  Accountability Humility</text>
  <text class="attr" x="668" y="546" font-size="13" textLength="230" lengthAdjust="spacingAndGlyphs">Decisive Curious  Integrity  Caring</text>

  <!-- capitalism -->
  <text class="value value--navy" x="76" y="620" font-size="76" textLength="263" lengthAdjust="spacingAndGlyphs">CAPITALISM</text>
  <rect class="tile-red" x="348" y="560" width="500" height="55"/>
  <path class="tile-navy" d="M846 560 H892 V615 H829 Z" role="img" aria-label="Hand holding a coin icon"/>
  <text class="attr attr--light" x="358" y="586" font-size="17" textLength="411" lengthAdjust="spacingAndGlyphs">Honorable  Cunning  Competitive Perseverance</text>
  <text class="attr attr--light" x="358" y="607" font-size="17" textLength="466" lengthAdjust="spacingAndGlyphs">Compartmentalization  Conscientiousness  Innovative</text>
</svg>
</body>
</html>
```